New residential property management company

I have a lot of name recognition in our smaller town due to owning a construction company here. I have now started a residential property management company representing landlords and tenants. Just trying to get my name out there and get some rentals to manage!

```html
<!DOCTYPE html>
<html lang="en">
<head>
<meta charset="utf-8">
<title>Harlan Property Management – Postcard</title>
<link rel="stylesheet" href="https://fonts.googleapis.com/css2?family=Poppins:wght@400;500;600;700;800;900&display=swap">
<style>
  :root {
    --page: #dcdcdc;
    --ink: #111018;
    --indigo: #2d1f6b;
    --indigo-deep: #24185c;
    --violet: #4b2fa0;
    --violet-mid: #5a45b4;
    --lavender: #8f83d0;
    --phone: #a49ad8;
    --rule: #5b4ca6;
    --white: #ffffff;
    --stamp: #ebebeb;
    --line: #cfcfcf;
  }
  * { box-sizing: border-box; margin: 0; padding: 0; }
  html, body { width: 692px; height: 1200px; overflow: hidden; }
  body {
    background: var(--page);
    font-family: "Poppins", sans-serif;
    position: relative;
  }
  .postcard {
    position: absolute;
    left: 26px;
    width: 640px;
    height: 426px;
    background: var(--white);
    overflow: hidden;
    box-shadow: 0 6px 14px rgba(0,0,0,.22);
  }
  .postcard--front { top: 110px; }
  .postcard--back  { top: 640px; }
  .abs { position: absolute; }
  .shapes { position: absolute; inset: 0; width: 640px; height: 426px; }

  /* brand lockup */
  .brand { display: flex; align-items: center; gap: 9px; }
  .brand__mark { width: 30px; height: 30px; background: var(--ink); }
  .brand__text { font-weight: 500; color: var(--ink); line-height: 1; }
  .brand__name { font-size: 38px; letter-spacing: 1px; display: block; }
  .brand__sub { font-size: 6px; letter-spacing: 1.6px; display: block; margin-top: 3px; text-align: right; }

  /* front */
  .house-photo {
    left: 250px; top: 0; width: 390px; height: 285px;
    background: linear-gradient(90deg, rgba(255,255,255,1) 0%, rgba(226,230,240,.9) 22%, #cfc8b6 45%, #bdb4a0 70%, #a9a6a8 100%);
  }
  .sky-fade {
    left: 250px; top: 0; width: 390px; height: 120px;
    background: linear-gradient(180deg, rgba(150,170,215,.55), rgba(255,255,255,0));
  }
  .agent-photo {
    left: 462px; top: 170px; width: 160px; height: 256px;
    border-radius: 80px 80px 0 0;
    background: linear-gradient(180deg, #2a2630 0%, #121116 100%);
  }
  .headline {
    left: 28px; top: 100px;
    border-left: 3px solid var(--indigo);
    padding-left: 15px;
    font-weight: 800;
    color: var(--ink);
  }
  .headline span { display: block; white-space: nowrap; }
  .headline .h-sm { font-size: 27px; line-height: 25px; letter-spacing: -.3px; }
  .headline .h-lg { font-size: 38px; line-height: 33px; color: var(--indigo); font-weight: 900; letter-spacing: -.5px; }
  .headline .h-lg.dark { color: var(--ink); }
  .tagline {
    left: 27px; top: 222px;
    font-size: 21px; font-weight: 600; line-height: 24px; color: var(--violet);
    white-space: nowrap;
  }
  .contact-label {
    font-weight: 700; color: var(--white);
  }
  .front-contact-label { left: 27px; top: 300px; font-size: 19px; }
  .agent-name {
    left: 185px; top: 287px; width: 265px; height: 33px;
    background: var(--ink);
    clip-path: polygon(0 0, 100% 0, 92% 100%, 0 100%);
    border-radius: 5px 0 0 5px;
    color: var(--white); font-weight: 800; font-size: 24px;
    padding-left: 18px; line-height: 33px;
  }
  .rule { height: 1px; background: var(--rule); }
  .front-rule { left: 27px; top: 328px; width: 415px; }
  .contact-list { list-style: none; }
  .contact-list li { display: flex; align-items: center; gap: 14px; color: var(--white); white-space: nowrap; }
  .icon {
    width: 16px; height: 16px; border-radius: 50%;
    background: var(--rule);
    display: flex; align-items: center; justify-content: center; flex: none;
  }
  .icon svg { width: 9px; height: 9px; }
  .front-contacts { left: 27px; top: 338px; }
  .front-contacts .web { font-size: 12px; height: 20px; }
  .front-contacts .phone { font-size: 26px; font-weight: 800; color: var(--phone); height: 30px; }
  .front-contacts .email { font-size: 12px; font-weight: 600; height: 20px; }
  .web b { font-weight: 700; }
  .web .faint { color: var(--lavender); }
  .social-tile {
    left: 503px; top: 383px; width: 20px; height: 20px;
    background: var(--ink); border-radius: 3px;
  }

  /* back */
  .services-title {
    left: 28px; top: 27px; width: 146px; height: 25px;
    background: var(--ink); border-radius: 4px;
    color: var(--white); font-weight: 800; font-size: 15px;
    text-align: center; line-height: 25px;
  }
  .services { left: 28px; top: 0; list-style: none; }
  .services li {
    position: absolute; left: 0; width: 200px;
    font-size: 11px; line-height: 12px; color: var(--ink);
    padding-left: 20px; white-space: nowrap;
  }
  .services li .tick {
    position: absolute; left: 0; top: 1px;
    width: 9px; height: 9px; border-radius: 50%; background: var(--violet);
  }
  .model-house {
    left: 214px; top: 28px; width: 200px; height: 185px;
    border-radius: 0 30px 30px 0;
    background: linear-gradient(135deg, #e9ecef 0%, #cfd6df 40%, #6d7583 70%, #7ea36b 100%);
  }
  .stamp { left: 522px; top: 27px; width: 90px; height: 90px; background: var(--stamp); border-radius: 6px; }
  .address-line { left: 430px; width: 182px; height: 1px; background: var(--line); }
  .back-contact-label { left: 29px; top: 315px; font-size: 15px; }
  .back-rule { left: 29px; top: 336px; width: 160px; }
  .back-contacts { left: 29px; top: 342px; }
  .back-contacts li { gap: 6px; }
  .back-contacts .icon { width: 12px; height: 12px; }
  .back-contacts .icon svg { width: 7px; height: 7px; }
  .back-contacts .phone { font-size: 20px; font-weight: 800; color: var(--phone); height: 25px; }
  .back-contacts .email { font-size: 10px; font-weight: 600; height: 16px; }
  .back-contacts .web { font-size: 10px; height: 16px; }
  .back-brand { left: 410px; top: 312px; }
  .back-brand .brand__mark { width: 26px; height: 26px; }
  .back-brand .brand__name { font-size: 32px; }
  .back-brand .brand__sub { font-size: 5px; }
  .address { left: 338px; top: 375px; display: flex; align-items: center; gap: 8px; font-size: 11px; color: var(--ink); white-space: nowrap; }
  .address svg { width: 12px; height: 15px; }
</style>
</head>
<body>

<section class="postcard postcard--front" aria-label="Postcard front">
  <div class="abs house-photo" role="img" aria-label="Photo of a row of new two-storey residential houses"></div>
  <div class="abs sky-fade"></div>

  <svg class="shapes" viewBox="0 0 640 426" aria-hidden="true">
    <polygon points="0,272 640,240 640,262 0,284" fill="#7d6fc6" opacity=".75"/>
    <polygon points="0,283 640,258 640,426 0,426" fill="var(--indigo)"/>
    <path d="M430,426 L600,200 Q640,150 640,150 L640,426 Z" fill="var(--violet-mid)"/>
    <path d="M560,426 L640,300 L640,426 Z" fill="#6b53c6"/>
    <path d="M520,200 Q560,150 600,120 L640,95 L640,250 L560,330 Z" fill="var(--violet)"/>
    <path d="M390,426 L470,330 Q480,318 492,318 L560,318 L470,426 Z" fill="var(--violet)" opacity=".85"/>
  </svg>

  <div class="abs agent-photo" role="img" aria-label="Portrait photo of the agent, Marissa Harlan"></div>

  <div class="abs brand" style="left:24px; top:30px;">
    <span class="brand__mark"></span>
    <span class="brand__text">
      <span class="brand__name">HARLAN</span>
      <span class="brand__sub">PROPERTY MANAGEMENT LLC.</span>
    </span>
  </div>

  <h1 class="abs headline">
    <span class="h-sm">NEW RESIDENTIAL</span>
    <span class="h-lg">PROPERTY</span>
    <span class="h-sm">MANAGEMENT</span>
    <span class="h-lg dark">COMPANY</span>
  </h1>
  <p class="abs tagline">Representing Landlords<br>and Tenants</p>

  <p class="abs contact-label front-contact-label">Contact now!</p>
  <p class="abs agent-name">Marissa Harlan</p>
  <div class="abs rule front-rule"></div>

  <ul class="abs contact-list front-contacts">
    <li class="web">
      <span class="icon"><svg viewBox="0 0 10 10"><circle cx="5" cy="5" r="4" fill="none" stroke="#fff" stroke-width="1"/><path d="M1 5h8M5 1c2 2 2 6 0 8M5 1c-2 2-2 6 0 8" fill="none" stroke="#fff" stroke-width=".8"/></svg></span>
      <span><span class="faint">www.</span><b>harlanpropertymanagement</b><span class="faint">.com</span></span>
    </li>
    <li class="phone">
      <span class="icon"><svg viewBox="0 0 10 10"><path d="M2 1l2 2-1 1.2c.6 1.3 1.5 2.2 2.8 2.8L7 6l2 2-1.3 1.3C4.5 9 1 5.5.7 2.3Z" fill="#fff"/></svg></span>
      <span>541-555-0187</span>
    </li>
    <li class="email">
      <span class="icon"><svg viewBox="0 0 10 10"><rect x="1" y="2" width="8" height="6" fill="#fff"/><path d="M1 2l4 3.5L9 2" fill="none" stroke="var(--rule)" stroke-width=".9"/></svg></span>
      <span>harlanpropertymanagement@mail.com</span>
    </li>
  </ul>
  <div class="abs social-tile" aria-label="Social media"></div>
</section>

<section class="postcard postcard--back" aria-label="Postcard back">
  <svg class="shapes" viewBox="0 0 640 426" aria-hidden="true">
    <polygon points="0,175 0,300 90,250" fill="#7d6fc6" opacity=".8"/>
    <path d="M250,270 L330,200 Q345,188 360,200 L385,225 L300,300 Z" fill="var(--violet-mid)" opacity=".85"/>
    <path d="M300,300 L380,230 Q395,220 405,230 L440,265 Q448,275 438,285 L355,355 Z" fill="#b7addf" opacity=".7"/>
    <path d="M210,255 L300,170 Q325,150 345,170 L360,185 L260,285 Z" fill="var(--violet)" opacity=".9"/>
    <path d="M0,300 L98,232 Q110,222 124,232 L345,426 L0,426 Z" fill="var(--indigo-deep)"/>
    <path d="M0,360 L60,320 L165,426 L0,426 Z" fill="var(--violet)" opacity=".35"/>
  </svg>

  <div class="abs model-house" role="img" aria-label="Photo of a small model house with a set of keys"></div>

  <h2 class="abs services-title">OUR SERVICES</h2>
  <ul class="abs services">
    <li style="top:67px;"><span class="tick"></span>Take photos and post pictures<br>of listings</li>
    <li style="top:101px;"><span class="tick"></span>Reply to potential buyers and<br>sellers vial social media</li>
    <li style="top:132px;"><span class="tick"></span>Post daily content to<br>engage target market</li>
    <li style="top:166px;"><span class="tick"></span>Hashtag research</li>
    <li style="top:189px;"><span class="tick"></span>Need something<br>else? just ask!</li>
  </ul>

  <div class="abs stamp" aria-label="Stamp area"></div>
  <div class="abs address-line" style="top:177px;"></div>
  <div class="abs address-line" style="top:214px;"></div>
  <div class="abs address-line" style="top:250px;"></div>

  <p class="abs contact-label back-contact-label">Contact now!</p>
  <div class="abs rule back-rule"></div>
  <ul class="abs contact-list back-contacts">
    <li class="phone">
      <span class="icon"><svg viewBox="0 0 10 10"><path d="M2 1l2 2-1 1.2c.6 1.3 1.5 2.2 2.8 2.8L7 6l2 2-1.3 1.3C4.5 9 1 5.5.7 2.3Z" fill="#fff"/></svg></span>
      <span>541-555-0187</span>
    </li>
    <li class="email">
      <span class="icon"><svg viewBox="0 0 10 10"><rect x="1" y="2" width="8" height="6" fill="#fff"/></svg></span>
      <span>harlanpropertymanagement@mail.com</span>
    </li>
    <li class="web">
      <span class="icon"><svg viewBox="0 0 10 10"><circle cx="5" cy="5" r="4" fill="none" stroke="#fff" stroke-width="1"/></svg></span>
      <span><span class="faint">www.</span><b>harlanpropertymanagement</b><span class="faint">.com</span></span>
    </li>
  </ul>

  <div class="abs brand back-brand">
    <span class="brand__mark"></span>
    <span class="brand__text">
      <span class="brand__name">HARLAN</span>
      <span class="brand__sub">PROPERTY MANAGEMENT LLC.</span>
    </span>
  </div>
  <p class="abs address">
    <svg viewBox="0 0 12 15"><path d="M6 0C2.7 0 0 2.6 0 5.8 0 10 6 15 6 15s6-5 6-9.2C12 2.6 9.3 0 6 0Z" fill="var(--violet)"/><circle cx="6" cy="5.8" r="2.2" fill="#fff"/></svg>
    218 Alder Ridge Rd Millbrook, OR 97400
  </p>
</section>

</body>
</html>
```